Velmi Corporate Website for technological company

We need a modern website to promote our product and services.
You can found the actually website at the address: www.velmi-example.ch

We are a new company for B2B market. We would like do show our high precision and innovation capability.

we need a section were is possible to easily upload "news" and documents for our customers.

Target Market(s)

B2B services in the industry market

Industry/Entity Type

It Company

Coding

Coded - Design and coding required

Number of Pages Required

5+ page

Font styles to use
Other font styles liked:
• We accept propositions

Requirements
Must have
• Easy to maintain
• Presentation of the Velmi company
• Presentation of Velmi services and products
• The customer can download our ducumentation
Nice to have
• Sexy and modern

```html
<!DOCTYPE html>
<html lang="en">
<head>
<meta charset="utf-8">
<title>Velmi Sàrl – Technology</title>
<link rel="stylesheet" href="https://fonts.googleapis.com/css2?family=Open+Sans:wght@400;600;700&display=swap">
<style>
:root{
  --green:#0d6b1e;
  --green-dark:#0a5517;
  --olive:#a49f5d;
  --olive-soft:#b7b37e;
  --beige:#dedcc4;
  --ink:#222;
  --grey-dark:#3a3a3a;
  --white:#fff;
}
*{margin:0;padding:0;box-sizing:border-box}
html,body{width:1200px;height:2699px;overflow:hidden;background:var(--white);font-family:"Open Sans",Arial,sans-serif;color:var(--ink)}
.page{position:relative;width:1200px;height:2699px;overflow:hidden}
.abs{position:absolute}
/* header */
.header{left:0;top:0;width:1200px;height:90px;background:var(--white)}
.brand{left:252px;top:34px;font-size:26px;font-weight:700;color:var(--ink);display:flex;align-items:center;gap:8px}
.brand-mark{width:18px;height:18px;background:var(--olive)}
.nav a{position:absolute;top:48px;height:28px;line-height:28px;font-size:13px;color:var(--ink);text-decoration:none}
.nav .active{background:var(--green);color:var(--white);padding:0 18px}
.social{top:24px;left:800px;display:flex;gap:8px}
.social span{width:10px;height:10px;border-radius:50%;background:var(--green);display:block}
.lang{top:22px;left:868px;font-size:10px;display:flex;gap:8px;align-items:center}
.lang i{width:22px;height:13px;background:#2a3a8c;display:block}
/* hero */
.hero{left:0;top:90px;width:1200px;height:482px;background:radial-gradient(circle at 50% 25%,#6aa0c8 0,#9fb5c0 18%,#b9c0bd 40%,#7d8d80 100%),var(--grey-dark)}
.hero::before{content:"";position:absolute;left:0;top:0;width:100%;height:70px;background:linear-gradient(180deg,rgba(13,107,30,.85),rgba(13,107,30,0))}
.arrow{position:absolute;width:22px;height:36px}
/* section titles */
.title{position:absolute;width:300px;text-align:center;font-size:17px;font-weight:700;color:var(--green)}
.title svg{display:block;margin:8px auto 0}
/* services */
.services{left:0;top:572px;width:1200px;height:349px;background:var(--beige)}
.service-icon{position:absolute;width:126px;height:126px;border:2px solid var(--green);border-radius:50%;display:flex;align-items:center;justify-content:center}
.service-text{position:absolute;width:180px}
.service-text h3{font-size:13px;color:var(--green);margin-bottom:8px}
.service-text p{font-size:9.5px;line-height:1.45;color:var(--ink)}
.btn-outline{display:inline-block;margin-top:12px;border:1.5px solid var(--green);font-size:8.5px;padding:3px 12px;color:var(--green);background:var(--beige)}
.dots{position:absolute;display:flex;gap:6px}
.dots span{width:10px;height:10px;border:1.5px solid var(--green);display:block}
.dots .on{background:var(--green)}
/* products */
.products{left:0;top:921px;width:1200px;height:417px;background:linear-gradient(90deg,#9fa995 0,#aab39c 45%,#b5a898 70%,#9aa48e 100%)}
.card{position:absolute;width:162px;top:88px}
.card-photo{height:202px}
.card-buy{height:36px;background:var(--olive);color:var(--white);font-size:14px;display:flex;justify-content:center;align-items:center;gap:30px}
/* examples */
.examples{left:0;top:1338px;width:1200px;height:420px;background:var(--white)}
.example-photo{left:0;top:0;width:587px;height:420px;background:linear-gradient(135deg,#c9c9c9,#7b7b7b 55%,#999)}
.example-box{left:552px;top:103px;width:268px;height:268px;background:rgba(184,180,127,.92);border:2px solid #2d2d1e;padding:16px 20px;text-align:center}
.example-box h3{font-size:15px;color:var(--green);margin-bottom:14px}
.example-box p{font-size:9.5px;line-height:1.6;margin-bottom:10px}
/* download */
.download{left:0;top:1758px;width:1200px;height:419px;background:radial-gradient(circle at 60% 40%,#3d4c52,#1f2324 70%)}
.doc{position:absolute;top:145px;width:213px}
.doc-label{font-size:7.5px;color:var(--white);text-align:right;font-weight:700;height:10px}
.doc-photo{height:153px;border:2px solid var(--white)}
.doc-caption{font-size:9px;color:var(--white);font-weight:700;margin-top:8px}
/* contact */
.contact{left:0;top:2177px;width:1200px;height:315px;background:linear-gradient(180deg,#273a48,#232628)}
.contact h2{position:absolute;font-size:16px;color:var(--white);font-weight:700}
.office{left:250px;top:96px;font-size:10px;color:var(--white);line-height:1.6}
.office div{display:flex;gap:10px;margin-bottom:6px}
.office b{color:#3fae4a;font-weight:700;width:8px}
.field{position:absolute;left:518px;width:432px;height:22px;border:1px solid #c7c7c7;font-size:8px;color:var(--white);padding:4px 6px}
.send{left:698px;top:250px;width:76px;height:18px;background:var(--olive-soft);color:var(--green);font-size:8px;font-weight:700;text-align:center;line-height:18px}
/* footer */
.footer{left:0;top:2492px;width:1200px;height:185px;background:var(--grey-dark)}
.footer h4{position:absolute;font-size:14px;color:var(--olive-soft);font-weight:700}
.footer p,.footer li{font-size:8.5px;color:var(--white);line-height:1.5;list-style:none}
.divider{position:absolute;top:40px;width:1px;height:120px;background:#777}
.thumb{position:absolute;top:55px;height:58px;border:2px solid var(--white);background:linear-gradient(135deg,#d9d9d9,#8c8c8c)}
.more{left:822px;top:127px;width:87px;height:20px;background:var(--olive-soft);color:var(--green-dark);font-size:8px;font-weight:700;text-align:center;line-height:20px}
.bottom-bar{left:0;top:2677px;width:1200px;height:22px;background:var(--green);color:var(--white);font-size:8px;line-height:22px;padding-left:248px}
</style>
</head>
<body>
<div class="page">

  <header class="abs header">
    <div class="abs brand"><span class="brand-mark"></span>Velmi Sàrl</div>
    <nav class="nav">
      <a class="active" style="left:473px">Home</a>
      <a style="left:561px">Servies</a>
      <a style="left:633px">Products</a>
      <a style="left:716px">Examples</a>
      <a style="left:803px">Download</a>
      <a style="left:895px">Contact Us</a>
    </nav>
    <div class="abs social"><span></span><span></span><span></span></div>
    <div class="abs lang">English <i></i>
      <svg width="9" height="6"><polygon points="0,0 9,0 4.5,6" fill="#222"/></svg></div>
  </header>

  <section class="abs hero" role="img" aria-label="Hand holding a circuit board under a globe, surrounded by mechanical parts, a parcel and business figures">
    <svg class="arrow" style="left:108px;top:243px" viewBox="0 0 22 36"><polyline points="18,3 4,18 18,33" fill="none" stroke="#0d6b1e" stroke-width="5"/></svg>
    <svg class="arrow" style="left:972px;top:243px" viewBox="0 0 22 36"><polyline points="4,3 18,18 4,33" fill="none" stroke="#0d6b1e" stroke-width="5"/></svg>
  </section>

  <section class="abs services">
    <svg class="abs" style="left:0;top:0" width="1200" height="349">
      <polygon points="396,0 801,0 600,165" fill="#fff"/>
      <polygon points="600,220 396,349 801,349" fill="#fff"/>
    </svg>
    <div class="title" style="left:450px;top:26px">SERVIES
      <svg width="160" height="22"><line x1="0" y1="11" x2="62" y2="11" stroke="#0d6b1e"/><line x1="98" y1="11" x2="160" y2="11" stroke="#0d6b1e"/><path d="M72 3 L88 19 M88 3 L72 19" stroke="#0d6b1e" stroke-width="3"/></svg>
    </div>
    <svg class="arrow" style="left:240px;top:168px" viewBox="0 0 22 36"><polyline points="16,6 6,18 16,30" fill="none" stroke="#0d6b1e" stroke-width="3"/></svg>
    <svg class="arrow" style="left:942px;top:168px" viewBox="0 0 22 36"><polyline points="6,6 16,18 6,30" fill="none" stroke="#0d6b1e" stroke-width="3"/></svg>

    <div class="service-icon" style="left:270px;top:121px">
      <svg width="56" height="56" viewBox="0 0 56 56"><circle cx="28" cy="28" r="17" fill="none" stroke="#0d6b1e" stroke-width="10" stroke-dasharray="7 4"/><circle cx="28" cy="28" r="11" fill="#0d6b1e"/><circle cx="28" cy="28" r="5" fill="#dedcc4"/></svg>
    </div>
    <div class="service-text" style="left:408px;top:125px">
      <h3>Software design</h3>
      <p>Modern electrical systems are built around microcontrollers and other logic units that require the development of specific software.</p>
      <span class="btn-outline">Read Now</span>
    </div>

    <div class="service-icon" style="left:621px;top:121px">
      <svg width="56" height="50" viewBox="0 0 56 50"><rect x="12" y="4" width="38" height="28" fill="none" stroke="#0d6b1e" stroke-width="3"/><line x1="12" y1="11" x2="50" y2="11" stroke="#0d6b1e" stroke-width="3"/><path d="M2 36 Q14 30 26 38 L42 36 Q46 40 40 44 L6 46 Z" fill="#0d6b1e"/></svg>
    </div>
    <div class="service-text" style="left:760px;top:125px">
      <h3>Embedded software</h3>
      <p>The development of such a firmware requires a detailed knowledge of the logic units and their dedicated language, as well as the system being controlled and the</p>
      <span class="btn-outline">Read Now</span>
    </div>
    <div class="dots" style="left:580px;top:306px"><span class="on"></span><span></span><span class="on"></span></div>
  </section>

  <section class="abs products" role="img" aria-label="Engineer's hand reaching toward a row of product tiles">
    <div class="title" style="left:450px;top:30px">PRODUCTS
      <svg width="160" height="22"><line x1="0" y1="11" x2="62" y2="11" stroke="#0d6b1e"/><line x1="98" y1="11" x2="160" y2="11" stroke="#0d6b1e"/><path d="M72 3 L88 19 M88 3 L72 19" stroke="#0d6b1e" stroke-width="3"/></svg>
    </div>
    <svg class="arrow" style="left:234px;top:195px" viewBox="0 0 22 36"><polyline points="16,6 6,18 16,30" fill="none" stroke="#0d6b1e" stroke-width="3"/></svg>
    <svg class="arrow" style="left:944px;top:195px" viewBox="0 0 22 36"><polyline points="6,6 16,18 6,30" fill="none" stroke="#0d6b1e" stroke-width="3"/></svg>
    <div class="card" style="left:274px"><div class="card-photo" role="img" aria-label="Hands soldering a circuit board" style="background:linear-gradient(135deg,#3a5a8a,#b0864e)"></div><div class="card-buy"><span>Buy</span><span>$.28.12</span></div></div>
    <div class="card" style="left:518px"><div class="card-photo" role="img" aria-label="Machined metal parts" style="background:linear-gradient(135deg,#e0e0e0,#7a7a7a)"></div><div class="card-buy"><span>Buy</span><span>$.28.12</span></div></div>
    <div class="card" style="left:765px"><div class="card-photo" role="img" aria-label="Opened hard drive mechanism" style="background:linear-gradient(135deg,#d5d5d5,#6c5a40)"></div><div class="card-buy"><span>Buy</span><span>$.28.12</span></div></div>
    <div class="dots" style="left:580px;top:366px"><span class="on"></span><span class="on"></span><span class="on"></span></div>
  </section>

  <section class="abs examples">
    <div class="abs example-photo" role="img" aria-label="Precision camera and microscope inspection station"></div>
    <svg class="abs" style="left:0;top:0" width="1200" height="420">
      <polygon points="587,0 882,0 587,260" fill="#fff"/>
      <polygon points="882,0 1200,0 1200,420 700,420 587,300 587,260" fill="#b5b27c"/>
      <polygon points="587,300 700,420 587,420" fill="#fff"/>
    </svg>
    <div class="title" style="left:534px;top:42px">EXAMPLES
      <svg width="160" height="22"><line x1="0" y1="11" x2="62" y2="11" stroke="#0d6b1e"/><line x1="98" y1="11" x2="160" y2="11" stroke="#0d6b1e"/><path d="M72 3 L88 19 M88 3 L72 19" stroke="#0d6b1e" stroke-width="3"/></svg>
    </div>
    <div class="abs example-box">
      <h3>RÉSULTATS OBTENUS</h3>
      <p>L'étape la plus importante et la plus compliquée était le dévelop-pement et l'écriture des algorithmes de gestion de trajectoires sur une sphère. Ces algorithmes permettent un contrôle précise et rapides de la position de la sphère.</p>
      <p>L'électronique développée contrôle directement les 3 moteurs électriques (interpolation précise des trajectoires).</p>
      <span class="btn-outline" style="background:transparent">Read Now</span>
    </div>
  </section>

  <section class="abs download" role="img" aria-label="Hands working on a tablet over a dark technology backdrop">
    <div class="title" style="left:450px;top:62px;color:#fff">DOWNLOAD
      <svg width="160" height="22"><line x1="0" y1="11" x2="62" y2="11" stroke="#fff"/><line x1="98" y1="11" x2="160" y2="11" stroke="#fff"/><path d="M72 3 L88 19 M88 3 L72 19" stroke="#fff" stroke-width="3"/></svg>
    </div>
    <svg class="abs" style="left:249px;top:125px" width="14" height="14"><circle cx="7" cy="7" r="5.5" fill="none" stroke="#fff" stroke-width="1.5"/></svg>
    <div class="doc" style="left:248px;top:135px"><div class="doc-label">DOWNLOAD</div><div class="doc-photo" role="img" aria-label="Green controller board" style="background:linear-gradient(135deg,#e9ece6,#3d8a4d)"></div><div class="doc-caption">PHOTO SAMPLE 16MB</div></div>
    <div class="doc" style="left:493px;top:135px"><div class="doc-label">DOWNLOAD</div><div class="doc-photo" role="img" aria-label="Green circuit board with magnifier overlay" style="background:linear-gradient(135deg,#7ecf7e,#4aa54f)"></div><div class="doc-caption">PHOTO SAMPLE 20MB</div></div>
    <div class="doc" style="left:738px;top:135px"><div class="doc-label">DOWNLOAD</div><div class="doc-photo" role="img" aria-label="Boxed device with cable" style="background:linear-gradient(135deg,#f1f1f1,#b5b5b5)"></div><div class="doc-caption">PHOTO SAMPLE 28MB</div></div>
    <div class="dots" style="left:580px;top:360px"><span style="border-color:#fff"></span><span style="border-color:#fff;background:#fff"></span><span style="border-color:#fff;background:#fff"></span></div>
  </section>

  <section class="abs contact">
    <h2 style="left:248px;top:45px">Head Office – Velmi, China</h2>
    <div class="abs office">
      <div><b>&#9679;</b><span>Chemin des Vergers 8<br>CH - 1700 Fribourg</span></div>
      <div><b>&#9993;</b><span>Email: info@velmi-example.ch</span></div>
      <div><b>&#9742;</b><span>Phone: 41 (0)26 000 00 00</span></div>
    </div>
    <h2 style="left:682px;top:45px">Contact &nbsp;Us</h2>
    <div class="field" style="top:92px">Name :</div>
    <div class="field" style="top:124px">Email :</div>
    <div class="field" style="top:157px">Phone :</div>
    <div class="field" style="top:186px;height:50px">Message</div>
    <div class="abs send">SEND</div>
  </section>

  <footer class="abs footer">
    <h4 style="left:248px;top:42px">INTRODUCTION</h4>
    <p class="abs" style="left:248px;top:66px;width:145px">VELMI Sàrl a été mandatée pour aider une entreprise spécialisée dans l'inspection de petits composants mécaniques pour développer un convoyeur de haute précision. Ce convoyeur est utilisé pour déplacer des composants horlogers sous une caméra.</p>
    <div class="divider" style="left:400px"></div>
    <h4 style="left:430px;top:42px">FIND US</h4>
    <p class="abs" style="left:430px;top:66px">Chemin des Vergers 8<br><br>CH - 1700 Fribourg<br><br>Email: info@velmi-example.ch<br><br>Phone: 41 (0)26 000 00 00</p>
    <div class="divider" style="left:576px"></div>
    <h4 style="left:630px;top:42px">USEFUL</h4>
    <ul class="abs" style="left:630px;top:66px"><li>Home</li><li>Servies</li><li>Products</li><li>Examples</li><li>Download</li><li>Contact Us</li></ul>
    <div class="divider" style="left:729px"></div>
    <h4 style="left:774px;top:30px">WHAT OUR STUDENTS SAY</h4>
    <div class="thumb" style="left:774px;width:72px" role="img" aria-label="Metal ring part"></div>
    <div class="thumb" style="left:873px;width:77px" role="img" aria-label="Machined metal blocks"></div>
    <div class="abs more">MORE PHOTO</div>
  </footer>
  <div class="abs bottom-bar">© 2016 Velmi. ALL RIGHTS RESERVED.</div>

</div>
</body>
</html>
```